Business Card Design with a glossy effect please

We supply and install Glass pool fencing: in Frameless, Semi Frameless, and Stainless Steel we also install Glass Balustrading, interior and exterior, plus Aluminium Tubular and Gates and Screens, and Quorix QT2240 Glass protection

Business

Dale Moreton
M 0432918506 or T 08 9517 3264
Unit 3 / 41 Lindale Crescent, Wangara 6065
ABN: 51847203916
www.vistone-ky-poolfencing.com.au
info@vistone-ky-poolfencing.com.au

```html
<!DOCTYPE html>
<html lang="en">
<head>
<meta charset="utf-8">
<title>Vistone KY Pool Fencing – Business Card</title>
<link rel="stylesheet" href="https://fonts.googleapis.com/css2?family=Open+Sans:wght@400;600;700&display=swap">
<style>
  :root {
    --backdrop: #e4e6e8;
    --card: #ffffff;
    --navy: #0f4a72;
    --navy-deep: #0a3a5c;
    --cyan: #29b6e8;
    --ink: #3c4650;
    --muted: #7a8590;
  }
  * { box-sizing: border-box; margin: 0; padding: 0; }
  html, body {
    width: 1200px; height: 772px; overflow: hidden;
    background: var(--backdrop);
    font-family: "Open Sans", Arial, sans-serif;
  }
  .stage {
    position: relative; width: 1200px; height: 772px;
    display: flex; align-items: center; justify-content: center; gap: 60px;
  }
  .card {
    position: relative; width: 520px; height: 298px;
    background: var(--card);
    box-shadow: 0 6px 18px rgba(0,0,0,.14);
    overflow: hidden;
  }
  .brand {
    display: flex; align-items: center; gap: 10px;
    color: var(--navy); font-weight: 700; letter-spacing: .5px;
    white-space: nowrap;
  }
  .brand-mark { width: 18px; height: 18px; background: var(--cyan); flex: none; }
  .card-front .brand {
    position: absolute; left: 50%; top: 50%;
    transform: translate(-50%, -50%); font-size: 28px;
  }
  .card-back .brand {
    position: absolute; left: 50%; top: 58px;
    transform: translateX(-50%); font-size: 22px;
  }
  .name-band {
    position: absolute; left: 0; right: 0; top: 122px; height: 46px;
    background: linear-gradient(180deg, #1a5e8c 0%, var(--navy) 50%, var(--navy-deep) 100%);
    border-top: 3px solid var(--card); border-bottom: 3px solid var(--card);
    box-shadow: 0 -2px 0 var(--cyan), 0 2px 0 var(--cyan);
    display: flex; align-items: center; justify-content: center;
    color: #fff; font-size: 16px;
  }
  .name-band .person { font-weight: 700; }
  .name-band .divider { margin: 0 8px; font-weight: 400; }
  .name-band .role { font-weight: 400; color: #cfe8f6; }
  .contacts {
    position: absolute; left: 24px; right: 24px; top: 196px;
    display: grid; grid-template-columns: auto auto; gap: 10px 18px;
    font-size: 10.5px; color: var(--ink);
  }
  .contact { display: flex; align-items: center; gap: 6px; white-space: nowrap; }
  .contact svg { width: 13px; height: 13px; flex: none; }
</style>
</head>
<body>
<main class="stage">

  <section class="card card-front" aria-label="Card front">
    <div class="brand"><span class="brand-mark"></span>VISTONE KY POOL FENCING</div>
  </section>

  <section class="card card-back" aria-label="Card back">
    <div class="brand"><span class="brand-mark"></span>VISTONE KY POOL FENCING</div>

    <div class="name-band">
      <span class="person">Dale Moreton</span><span class="divider">|</span><span class="role">Owner / C.E.O</span>
    </div>

    <div class="contacts">
      <div class="contact">
        <svg viewBox="0 0 14 14" aria-hidden="true"><circle cx="7" cy="7" r="7" fill="#0f4a72"/><path d="M4.6 3.6l1.3 1.3-.7 1a4.5 4.5 0 0 0 2.9 2.9l1-.7 1.3 1.3-.9.9C7.3 10.2 3.8 6.7 3.7 4.5z" fill="#fff"/></svg>
        M 0432918506
      </div>
      <div class="contact">
        <svg viewBox="0 0 14 14" aria-hidden="true"><circle cx="7" cy="7" r="7" fill="#0f4a72"/><path d="M7 3a2.4 2.4 0 0 1 2.4 2.4C9.4 7.4 7 10.6 7 10.6S4.6 7.4 4.6 5.4A2.4 2.4 0 0 1 7 3z" fill="#fff"/><circle cx="7" cy="5.4" r=".9" fill="#0f4a72"/></svg>
        Unit 3 / 41 Lindale Crescent, Wangara 6065
      </div>
      <div class="contact">
        <svg viewBox="0 0 14 14" aria-hidden="true"><circle cx="7" cy="7" r="7" fill="#0f4a72"/><path d="M4.6 3.6l1.3 1.3-.7 1a4.5 4.5 0 0 0 2.9 2.9l1-.7 1.3 1.3-.9.9C7.3 10.2 3.8 6.7 3.7 4.5z" fill="#fff"/></svg>
        T 08 9517 3264
      </div>
      <div class="contact">
        <svg viewBox="0 0 14 14" aria-hidden="true"><circle cx="7" cy="7" r="7" fill="#0f4a72"/><circle cx="7" cy="7" r="3.4" fill="none" stroke="#fff" stroke-width=".9"/><path d="M3.6 7h6.8M7 3.6c-1.6 2-1.6 4.8 0 6.8M7 3.6c1.6 2 1.6 4.8 0 6.8" fill="none" stroke="#fff" stroke-width=".8"/></svg>
        www.vistone-ky-poolfencing.com.au
      </div>
      <div class="contact">
        <svg viewBox="0 0 14 14" aria-hidden="true"><circle cx="7" cy="7" r="7" fill="#0f4a72"/><rect x="4" y="4.5" width="6" height="5" fill="none" stroke="#fff" stroke-width=".9"/><path d="M5.5 6.2h3M5.5 7.8h3" stroke="#fff" stroke-width=".8"/></svg>
        ABN 51847203916
      </div>
      <div class="contact">
        <svg viewBox="0 0 14 14" aria-hidden="true"><circle cx="7" cy="7" r="7" fill="#0f4a72"/><rect x="3.6" y="4.6" width="6.8" height="4.8" fill="none" stroke="#fff" stroke-width=".9"/><path d="M3.8 4.8L7 7.4l3.2-2.6" fill="none" stroke="#fff" stroke-width=".9"/></svg>
        info@vistone-ky-poolfencing.com.au
      </div>
    </div>
  </section>

</main>
</body>
</html>
```